Letterhead for 3 attorney Workers' Comp law firm

We are a 3 attorney law office. We specialize in Workers' Compensation. Our office represents workers who are injured on the job, and the estates of workers who are killed one the job.
When we started our office, we created our own letterhead & have been using it for years. We've just recently hired the 3rd attorney, and were going to just add his name to the letterhead, but have decided we wanted to get a professionally designed letterhead and business cards at this point.
We want something that looks clean and professional. It must look good in black and white because we often make multiple copies of our documents. We're hoping for a design that resonates confidence, reliability and experience.
The design must include the firm name: Dorrance & Pike, PLLC. We would like the PLLC to be small compared to the Dorrance & Pike graphic. We also want to incorporate the attorney names: Ulric Dorrance, Janet Pike, and Lyle Hagberg. Our current letterhead has our contact info in the footer at the bottom of the page. We like that design, but are open to the idea of having it at the top. We'll leave that at the discretion of the designer. Our contact info is as follows: 472 S. Larchmont Avenue, Suite 315 Kestrel Falls, OR 98117 Phone: 360-514-2967, Fax: 360-521-6079, and our website: www.dorrancepike-law.example
Target Market(s)
Clients, courts, other legal offices, doctors offices. These are the people who see our letterhead most frequently. It's not so much for marketing purposes, mainly so that we have a professional image when sending out documents.
Industry/Entity Type
Law Firm
Contact Information for Business Card
On the back of the business card: it can be designed, or be a template for filling in appointment reminder information (i.e. date, time, etc)
Colors
Designer to choose colors to be used in the design.
Requirements
Must have
- Must have our firm name at the top.
- Must include the attorney names.
- Must have all of our contact information (can be at top or bottom - whatever looks best with the design)
Nice to have
- A strong, confident design
Should not have
- We don't want the design to be playful, cartoony or busy.

```html
<!DOCTYPE html>
<html lang="en">
<head>
<meta charset="UTF-8">
<title>Dorrance &amp; Pike, PLLC — Business Card</title>
<link href="https://fonts.googleapis.com/css2?family=Cinzel:wght@700&family=Roboto:wght@400&family=Roboto+Condensed:wght@700&display=swap" rel="stylesheet">
<style>
  :root {
    --navy: #03325e;
    --paper: #f4f4f3;
    --ink: #454545;
    --rule: #6b6b6b;
    --white: #ffffff;
    --backdrop: #5d4b3b;
  }
  * { margin: 0; padding: 0; box-sizing: border-box; }
  html, body {
    width: 1200px;
    height: 960px;
    overflow: hidden;
    background: var(--backdrop);
  }
  .stage { position: relative; width: 1200px; height: 960px; }

  .card {
    position: absolute;
    width: 600px;
    height: 343px;
  }
  .card-front { left: 314px; top: 113px; background: var(--paper); }
  .card-back  { left: 311px; top: 472px; background: var(--navy); }

  .firm-name {
    position: absolute;
    right: 40px;
    top: 56px;
    font-family: 'Cinzel', serif;
    font-weight: 700;
    font-size: 26px;
    line-height: 1;
    color: var(--navy);
    white-space: nowrap;
  }
  .firm-name .suffix { font-size: 18px; }

  .accent-bar {
    position: absolute;
    left: 0;
    top: 196px;
    width: 12px;
    height: 31px;
    background: var(--navy);
  }
  .person-name {
    position: absolute;
    left: 39px;
    top: 202px;
    font-family: 'Roboto Condensed', sans-serif;
    font-weight: 700;
    font-size: 21px;
    line-height: 1;
    color: var(--navy);
  }
  .divider {
    position: absolute;
    left: 39px;
    top: 233px;
    width: 521px;
    height: 1px;
    background: var(--rule);
  }

  .contact-list {
    position: absolute;
    left: 39px;
    top: 247px;
    list-style: none;
    font-family: 'Roboto', sans-serif;
    font-size: 14.5px;
    color: var(--ink);
  }
  .contact-list li {
    display: flex;
    align-items: center;
    height: 19px;
  }
  .contact-list svg {
    width: 14px;
    height: 14px;
    margin-right: 9px;
    fill: var(--navy);
  }

  .address {
    position: absolute;
    right: 39px;
    top: 267px;
    text-align: right;
    font-family: 'Roboto', sans-serif;
    font-style: normal;
    font-size: 14.5px;
    line-height: 19px;
    color: var(--ink);
  }

  .back-firm-name {
    position: absolute;
    right: 41px;
    top: 264px;
    font-family: 'Cinzel', serif;
    font-weight: 700;
    font-size: 21px;
    line-height: 1;
    color: var(--white);
    white-space: nowrap;
  }
  .back-website {
    position: absolute;
    right: 38px;
    top: 290px;
    font-family: 'Roboto', sans-serif;
    font-size: 14px;
    letter-spacing: 3.4px;
    color: var(--white);
    white-space: nowrap;
  }
</style>
</head>
<body>
<div class="stage">

  <section class="card card-front">
    <div class="firm-name">DORRANCE &amp; PIKE, <span class="suffix">PLLC</span></div>

    <div class="accent-bar"></div>
    <h1 class="person-name">ULRIC DORRANCE</h1>
    <div class="divider"></div>

    <ul class="contact-list">
      <li>
        <svg viewBox="0 0 16 16" aria-hidden="true"><path d="M3.6 1.2 6 3.6c.4.4.4 1 0 1.4L4.9 6.1c.8 1.8 3.2 4.2 5 5l1.1-1.1c.4-.4 1-.4 1.4 0l2.4 2.4c.4.4.4 1 0 1.4l-1.3 1.3c-.6.6-1.5.7-2.3.4C6.9 14 2 9.1.5 4.8.2 4 .3 3.1.9 2.5L2.2 1.2c.4-.4 1-.4 1.4 0z"/></svg>
        555-514-2967
      </li>
      <li>
        <svg viewBox="0 0 16 16" aria-hidden="true"><path d="M4 1h8v4H4z"/><path d="M1 6h14v6h-2.5v-2h-9v2H1z"/><path d="M4.5 11h7v4h-7z"/></svg>
        555-521-6079
      </li>
      <li>
        <svg viewBox="0 0 16 16" aria-hidden="true"><path d="M8 1a7 7 0 1 0 0 14A7 7 0 0 0 8 1zm-1 2.2c.6.5.4 1.3-.2 1.6-.8.4-1.5.9-1.2 1.8.3.8 1.5.6 2 1.3.4.6-.1 1.4.3 2 .4.6 1.2.8 1.1 1.7-.1.7-.6 1.3-1.2 1.4A5.5 5.5 0 0 1 4 4.2c1-.6 2-1 3-1zm3.5.9a5.5 5.5 0 0 1 2.4 6.2c-.5-.4-.9-1-1.6-1.1-.8-.1-1.3-.8-1.1-1.5.3-.9 1.1-1.3 1-2.2-.1-.6-.6-1-.7-1.4z"/></svg>
        www.dorrancepike-law.example
      </li>
    </ul>

    <address class="address">
      472 S. Larchmont Avenue<br>
      Suite 315 Kestrel Falls, OR 98117
    </address>
  </section>

  <section class="card card-back">
    <div class="back-firm-name">DORRANCE &amp; PIKE, PLLC</div>
    <div class="back-website">www.dorrancepike-law.example</div>
  </section>

</div>
</body>
</html>
```